Visitenkarte und Briefpapier für Rechtsanwaltskanzlei
Zielgruppe
Neugründung einer Rechtsanwaltskanzlei für Strafrecht mit einem Anwalt
Aufgabenstellung
Ich möchte gerne Briefpapier und Visitenkarten mit einem schlichten aber professionellen Charakter für meine neue Rechtsanwaltskanzlei erstellen lassen. Die Erscheinung soll modern, sachlich und klar sein. Es soll kein Logo verwendet werden, sondern nur der Namensschriftzug "Dr. Harald Obst", gerne in Großbuchstaben. Siehe dazu beispielhaft die Design-Charakter der angegeben Links.
Die Visitenkarte sollen als druckfähiges PDF und das Briefpapier zusätzlich als Word-Dokument geliefert werden.

```html
<!DOCTYPE html>
<html lang="de">
<head>
<meta charset="utf-8">
<title>Visitenkarte – Rechtsanwaltskanzlei Dr. Harald Obst</title>
<link rel="stylesheet" href="https://fonts.googleapis.com/css2?family=Inter:wght@300;400&display=swap">
<style>
  :root {
    --backdrop: #3b3b3b;
    --card: #f3f3f3;
    --card-edge: #e2e2e2;
    --ink: #2a2a2a;
    --ink-soft: #3c3c3c;
    --rule: #555555;
  }
  * { margin: 0; padding: 0; box-sizing: border-box; }
  html, body {
    width: 1200px;
    height: 1000px;
    overflow: hidden;
    background: var(--backdrop);
    font-family: "Inter", sans-serif;
  }
  .canvas {
    position: relative;
    width: 1200px;
    height: 1000px;
  }
  .card {
    position: absolute;
    background: linear-gradient(135deg, #ffffff 0%, var(--card) 45%, var(--card-edge) 100%);
    border-radius: 14px;
  }
  .card--contact {
    left: 180px; top: 169px;
    width: 530px; height: 302px;
  }
  .card--name {
    left: 473px; top: 549px;
    width: 528px; height: 303px;
  }
  .contact-block {
    position: absolute;
    left: 26px;
    top: 170px;
    font-size: 11px;
    line-height: 14.5px;
    color: var(--ink-soft);
    font-weight: 400;
  }
  .contact-block .divider {
    display: block;
    width: 9px;
    height: 1px;
    background: var(--ink-soft);
    margin: 6px 0 7px;
  }
  .wordmark {
    position: absolute;
    right: 25px;
    bottom: 36px;
    display: flex;
    flex-direction: column;
    align-items: stretch;
    text-align: right;
  }
  .wordmark__practice {
    font-size: 11px;
    letter-spacing: 4.2px;
    margin-right: -4.2px;
    color: var(--ink-soft);
    font-weight: 400;
    padding-bottom: 2px;
    border-bottom: 1px solid var(--rule);
  }
  .wordmark__name {
    font-size: 26px;
    font-weight: 300;
    color: var(--ink);
    letter-spacing: -0.3px;
    line-height: 30px;
    padding-top: 1px;
    white-space: nowrap;
  }
</style>
</head>
<body>
<main class="canvas">
  <section class="card card--contact" aria-label="Visitenkarte Rückseite">
    <div class="contact-block">
      <p>Dr. Harald Obst</p>
      <span class="divider"></span>
      <p>e: info@harald-obst.com</p>
      <p>t: +123 456 700 210</p>
      <span class="divider"></span>
      <p>12345 Musterstadt/Musterstrasse 2</p>
      <p>www.harald-obst.com</p>
    </div>
  </section>

  <section class="card card--name" aria-label="Visitenkarte Vorderseite">
    <div class="wordmark">
      <p class="wordmark__practice">RECHTSANWALTSKANZLEI</p>
      <p class="wordmark__name">Dr. HARALD OBST</p>
    </div>
  </section>
</main>
</body>
</html>
```